Vegan Alfredo Sauce Label Design for Bramble Pantry Co

We are a food co. committed to making vegan food more accessible to people who want to eat healthier. Our first line of product is vegan Alfredo sauce.
We have 3 flavors:
- Garlic
- Pesto
- Lemony Artichoke
The current project is the design for the first flavor: garlic. However, we would like a template that would translate well to other flavors, so they look like a family of products.
These will be in standard 16 oz jars. The whole label will be approx 6cm x 24cm, but the front visual space is approx 6cm x 10cm. The rest will be nutritional labeling and copy about the company.
We also need a stamp or font- based logo that says Bramble Pantry Co. (or lower case: bramble pantry co.), the name of the company.
The picture (attached) of Vegan Mimbo is the closest to what we are going for. Because the sauce is creamy white, a colorful background with off-white font will be best.
We currently have a website, although we are doing a brand over-haul (hence, this posting) www.bramblepantryco-example.com. If the designer is a good fit, we have several more projects, in line.
Other brands we love: Tidy Acres, Marlow Ridge Foods, Pulp Poured Daily.
The final brand should communicate hip, natural and health.
And personally, I love design that is clever and somehow makes me smile.
Target Market(s)
Vegans, vegetarians, and people with common food allergies - all ages.
Young, hip families.
Industry/Entity Type
It Company
Requirements
Must have
- Copy:
Vegan Alfredo or Vegan Alfredo Sauce
Garlic
Bramble Pantry or Bramble Pantry Co
16 oz
Nice to have
- May include copy:
Gluten-Free Soy-Free Nut-Free
Should not have
- Neon colors

```html
<!DOCTYPE html>
<html lang="en">
<head>
<meta charset="utf-8">
<title>Vegan Alfredo Sauce Label – Bramble Pantry Co.</title>
<link rel="stylesheet" href="https://fonts.googleapis.com/css2?family=Didact+Gothic&family=Source+Sans+3:wght@400;600;700&display=swap">
<style>
  :root {
    --page: #ffffff;
    --label-green: #c3df5c;
    --cream: #f8f1c8;
    --white: #ffffff;
    --garlic-orange: #e8742a;
    --bulb-tone: #eef3d6;
    --logo-brown: #7a3a1e;
    --logo-orange: #ef8a1c;
    --caption: #222222;
  }
  * { margin: 0; padding: 0; box-sizing: border-box; }
  html, body { width: 917px; height: 1200px; overflow: hidden; background: var(--page); }
  .canvas { position: relative; width: 917px; height: 1200px; }

  .label {
    position: absolute; left: 216px; top: 330px;
    width: 477px; height: 366px;
    background: var(--label-green);
    font-family: "Didact Gothic", sans-serif;
  }
  .label__title {
    position: absolute; left: 102px; top: 6px;
    color: var(--cream); line-height: 0.98;
  }
  .label__title span { display: block; }
  .label__title .line-vegan { font-size: 82px; }
  .label__title .line-alfredo { font-size: 76px; }
  .label__title .line-sauce { font-size: 92px; }

  .label__claims {
    position: absolute; right: 385px; top: 126px;
    font-family: "Source Sans 3", sans-serif; font-size: 18px;
    color: var(--white); text-align: right; line-height: 1.4; white-space: nowrap;
  }
  .label__flavour {
    position: absolute; left: 368px; top: 150px;
    font-family: "Source Sans 3", sans-serif; font-size: 27px;
    color: var(--garlic-orange);
  }
  .label__bulb {
    position: absolute; left: 384px; top: 188px;
    width: 54px; height: 72px; border-radius: 50% 50% 46% 46%;
    background: radial-gradient(circle at 50% 60%, var(--bulb-tone), var(--label-green));
  }
  .label__weight {
    position: absolute; left: 18px; top: 334px;
    font-family: "Source Sans 3", sans-serif; font-size: 14px; color: var(--white);
  }
  .label__brand {
    position: absolute; left: 356px; top: 312px; width: 118px;
    font-family: "Source Sans 3", sans-serif; font-weight: 600; font-size: 15px;
    line-height: 1.1; color: var(--logo-orange); text-align: center;
  }

  .logo-option { position: absolute; text-align: center; font-family: "Source Sans 3", sans-serif; }
  .logo-option__name { display: flex; align-items: center; justify-content: center; font-weight: 700; }
  .logo-option__caption { position: absolute; left: 0; right: 0; font-size: 14px; font-weight: 400; color: var(--caption); }

  .logo-option--alternative { left: 53px; top: 958px; width: 298px; height: 192px; }
  .logo-option--alternative .logo-option__name { height: 192px; font-size: 40px; line-height: 1.05; color: var(--logo-brown); }
  .logo-option--alternative .logo-option__caption { top: 210px; }

  .logo-option--rework { left: 423px; top: 978px; width: 459px; height: 160px; }
  .logo-option--rework .logo-option__name { height: 160px; font-size: 46px; color: var(--logo-orange); font-weight: 600; }
  .logo-option--rework .logo-option__caption { top: 178px; }
</style>
</head>
<body>
<main class="canvas">
  <section class="label" aria-label="Garlic vegan Alfredo sauce front label">
    <h1 class="label__title">
      <span class="line-vegan">Vegan</span>
      <span class="line-alfredo">Alfredo</span>
      <span class="line-sauce">Sauce</span>
    </h1>
    <p class="label__claims">Gluten-Free<br>Soy-Free<br>Nut-Free</p>
    <p class="label__flavour">Garlic</p>
    <div class="label__bulb" role="img" aria-label="Line illustration of a garlic bulb"></div>
    <p class="label__weight">16oz</p>
    <p class="label__brand">bramble pantry co.</p>
  </section>

  <figure class="logo-option logo-option--alternative">
    <div class="logo-option__name">Bramble Pantry Co.</div>
    <figcaption class="logo-option__caption">Logo alternative</figcaption>
  </figure>

  <figure class="logo-option logo-option--rework">
    <div class="logo-option__name">bramble pantry co.</div>
    <figcaption class="logo-option__caption">Logo rework</figcaption>
  </figure>
</main>
</body>
</html>
```